Security and Automation Company based in Texas and needs logo design also

Looking for a new logo design for our company - we are based in Texas and specialize in camera, security and home automation - We do want the main company name(Brightline Guard and Controls of Texas) with our parent company in small letters below (a Veloran Partners, LLC Company) and our License number needs to be included in the design - K74836 - Darker shades of blue preferred

Target Market(s)

We work with everyone from home to large corporate - so clean design would be helpful

Industry/Entity Type

It Company

Contact Information for Business Card

PO Box 4719
Cedar Hollow, Texas 75961
Leave a spot for the phone number and email address

Logo Text

Brightline Guard and Controls of Texas/a Veloran Partners Company/K74836

Font styles to use
Sans Serif

Colors
0255a3

```html
<!DOCTYPE html>
<html lang="en">
<head>
<meta charset="utf-8">
<title>Brightline Guard and Controls of Texas — Business Card</title>
<link rel="stylesheet" href="https://fonts.googleapis.com/css2?family=Marcellus+SC&family=Mulish:ital,wght@1,300;1,400&display=swap">
<style>
  :root {
    --backdrop: #b9b9bd;
    --navy: #0f2c85;
    --navy-deep: #0a1f66;
    --band: #1656a0;
    --paper: #ffffff;
    --paper-shade: #d9d9db;
    --ink-blue: #1e4f9a;
    --text-light: #ffffff;
  }
  html, body {
    margin: 0;
    width: 1200px;
    height: 1200px;
    overflow: hidden;
    background: var(--backdrop);
  }
  .canvas {
    position: relative;
    width: 1200px;
    height: 1200px;
  }
  .card {
    position: absolute;
    width: 638px;
    height: 364px;
    display: block;
  }
  .card--front { left: 131px; top: 195px; }
  .card--back  { left: 450px; top: 622px; }
  .license {
    font-family: "Marcellus SC", serif;
    font-size: 96px;
    fill: var(--text-light);
  }
  .company-name {
    font-family: "Marcellus SC", serif;
    font-size: 38px;
    fill: var(--text-light);
  }
  .company-name .small { font-size: 29px; }
  .parent-company {
    font-family: "Mulish", sans-serif;
    font-style: italic;
    font-weight: 300;
    font-size: 19px;
    fill: var(--text-light);
  }
  .contact {
    font-family: "Mulish", sans-serif;
    font-style: italic;
    font-weight: 300;
    font-size: 21px;
    fill: var(--ink-blue);
  }
</style>
</head>
<body>
<main class="canvas">

  <svg class="card card--front" viewBox="0 0 796 454" aria-label="Business card front">
    <defs>
      <linearGradient id="paperFront" x1="0" y1="0" x2="1" y2="0">
        <stop offset="0.25" stop-color="var(--paper-shade)"/>
        <stop offset="0.7" stop-color="var(--paper)"/>
      </linearGradient>
      <linearGradient id="navyFront" x1="0" y1="0" x2="1" y2="0.3">
        <stop offset="0.6" stop-color="var(--navy)"/>
        <stop offset="1" stop-color="var(--navy-deep)"/>
      </linearGradient>
      <filter id="liftFront" x="-5%" y="-5%" width="115%" height="115%">
        <feDropShadow dx="4" dy="4" stdDeviation="3" flood-color="#0a1f66" flood-opacity="0.6"/>
      </filter>
    </defs>
    <rect class="card-paper" width="796" height="454" fill="url(#paperFront)"/>
    <rect class="card-band" x="150" y="149" width="646" height="137" fill="var(--band)"/>
    <polygon class="card-wedge" points="0,0 116,0 398,454 0,454" fill="url(#navyFront)" filter="url(#liftFront)"/>
    <text class="license" x="778" y="257" text-anchor="end" filter="url(#liftFront)">K74836</text>
  </svg>

  <svg class="card card--back" viewBox="0 0 798 455" aria-label="Business card back">
    <defs>
      <linearGradient id="paperBack" x1="0" y1="0" x2="1" y2="0">
        <stop offset="0.25" stop-color="var(--paper-shade)"/>
        <stop offset="0.7" stop-color="var(--paper)"/>
      </linearGradient>
      <linearGradient id="navyBack" x1="0" y1="0" x2="1" y2="0.3">
        <stop offset="0.6" stop-color="var(--navy)"/>
        <stop offset="1" stop-color="var(--navy-deep)"/>
      </linearGradient>
      <filter id="liftBack" x="-5%" y="-5%" width="115%" height="115%">
        <feDropShadow dx="4" dy="4" stdDeviation="3" flood-color="#0a1f66" flood-opacity="0.6"/>
      </filter>
    </defs>
    <rect class="card-paper" width="798" height="455" fill="url(#paperBack)"/>
    <rect class="card-band" x="150" y="151" width="648" height="138" fill="var(--band)"/>
    <polygon class="card-wedge" points="0,0 116,0 399,455 0,455" fill="url(#navyBack)" filter="url(#liftBack)"/>
    <text class="company-name" x="766" y="206" text-anchor="end">BRIGHTLINE GUARD <tspan class="small">AND</tspan></text>
    <text class="company-name" x="788" y="240" text-anchor="end">CONTROLS <tspan class="small">OF</tspan> TEXAS</text>
    <text class="parent-company" x="532" y="268" text-anchor="middle">Veloran Partners LLC Company</text>
    <text class="contact" x="788" y="358" text-anchor="end">PO BOX 4719</text>
    <text class="contact" x="788" y="384" text-anchor="end">CEDAR HOLLOW, TEXAS 75961</text>
    <text class="contact" x="788" y="410" text-anchor="end">123-456-789</text>
    <text class="contact" x="788" y="437" text-anchor="end">EMAIL@EXAMPLE.COM</text>
  </svg>

</main>
</body>
</html>
```